Marrowby Electric
Business Cards
Marrowby Electric -
Creative Brief
Modern
Peter Marrowby
Owner
17 Orvell St. Brookfield CT. 06804
pete@marrowbyelectric-example.com
www.marrowbyelectric-example.com
E-1 #374620

```html
<!DOCTYPE html>
<html lang="en">
<head>
<meta charset="utf-8">
<title>Marrowby Electric – Business Cards</title>
<link rel="stylesheet" href="https://fonts.googleapis.com/css2?family=Roboto+Condensed:wght@400;700&display=swap">
<style>
  :root {
    --bg: #eceef1;
    --card-white: #ffffff;
    --navy-deep: #061a3d;
    --navy: #0b3a7a;
    --blue: #1d74c9;
    --blue-light: #3d9be6;
    --ink: #1d1d1f;
    --ink-soft: #4a4d55;
    --black-band: #0d0f14;
  }
  * { margin: 0; padding: 0; box-sizing: border-box; }
  html, body { width: 1200px; height: 646px; overflow: hidden; }
  body {
    background: var(--bg);
    font-family: "Roboto Condensed", Arial, sans-serif;
    position: relative;
  }
  .card {
    position: absolute;
    top: 174px;
    width: 520px;
    height: 297px;
    border-radius: 4px;
    overflow: hidden;
    box-shadow: 0 8px 24px rgba(0,0,0,0.18);
  }
  .card--back {
    left: 60px;
    background: radial-gradient(ellipse at 50% 40%, var(--blue) 0%, var(--navy) 45%, var(--navy-deep) 100%);
    display: flex;
    flex-direction: column;
    align-items: center;
    justify-content: center;
    gap: 14px;
  }
  .card--front {
    left: 620px;
    background: var(--card-white);
  }
  .brand-mark {
    width: 46px;
    height: 46px;
    border-radius: 6px;
    background: var(--blue-light);
  }
  .brand-name {
    font-weight: 700;
    text-transform: uppercase;
    letter-spacing: 1px;
    font-size: 30px;
    line-height: 1.05;
    text-align: center;
  }
  .brand-name span { display: block; }
  .card--back .brand-name { color: #ffffff; }
  .front-brand {
    position: absolute;
    left: 40px;
    top: 82px;
    width: 170px;
    display: flex;
    flex-direction: column;
    align-items: center;
    gap: 12px;
  }
  .front-brand .brand-name { color: var(--navy); font-size: 26px; }
  .swoosh {
    position: absolute;
    left: 0; top: 0;
    width: 520px; height: 297px;
  }
  .contact {
    position: absolute;
    left: 258px;
    top: 22px;
    width: 220px;
    color: var(--ink);
  }
  .contact__name {
    font-size: 19px;
    font-weight: 700;
    color: var(--blue);
  }
  .contact__role {
    font-size: 12px;
    color: var(--ink-soft);
    margin-bottom: 6px;
  }
  .contact__line {
    font-size: 11px;
    line-height: 1.45;
    color: var(--ink-soft);
    white-space: nowrap;
  }
  .contact__address { margin-top: 12px; }
  .contact__phone {
    display: flex;
    align-items: center;
    gap: 5px;
  }
  .contact__phone svg { width: 9px; height: 9px; fill: var(--blue); flex: none; }
  .website {
    position: absolute;
    right: 10px;
    bottom: 18px;
    writing-mode: vertical-rl;
    transform: rotate(180deg);
    font-size: 11px;
    letter-spacing: 0.5px;
    color: #ffffff;
  }
</style>
</head>
<body>

  <section class="card card--back" aria-label="Business card back">
    <div class="brand-mark"></div>
    <div class="brand-name"><span>Marrowby</span><span>Electric</span></div>
  </section>

  <section class="card card--front" aria-label="Business card front">
    <svg class="swoosh" viewBox="0 0 520 297" aria-hidden="true">
      <path d="M150 297 C 300 292, 420 250, 520 120 L520 297 Z" fill="var(--blue-light)"/>
      <path d="M190 297 C 330 290, 430 255, 520 150 L520 297 Z" fill="var(--black-band)"/>
      <path d="M300 297 C 400 285, 460 250, 500 200 L500 297 Z" fill="#1a1d24"/>
      <rect x="492" y="60" width="28" height="237" fill="var(--blue)"/>
    </svg>

    <div class="front-brand">
      <div class="brand-mark"></div>
      <div class="brand-name"><span>Marrowby</span><span>Electric</span></div>
    </div>

    <div class="contact">
      <div class="contact__name">Peter Marrowby</div>
      <div class="contact__role">Owner</div>
      <div class="contact__line">pete@marrowbyelectric-example.com</div>
      <div class="contact__line">License No: E-1 #374620</div>
      <div class="contact__line contact__address">17 Orvell St.</div>
      <div class="contact__line">Brookfield CT. 06804</div>
      <div class="contact__line contact__phone">
        <svg viewBox="0 0 24 24"><path d="M6.6 10.8a15.1 15.1 0 0 0 6.6 6.6l2.2-2.2c.3-.3.7-.4 1-.2 1.1.4 2.3.6 3.6.6.6 0 1 .4 1 1V20c0 .6-.4 1-1 1A17 17 0 0 1 3 4c0-.6.4-1 1-1h3.5c.6 0 1 .4 1 1 0 1.3.2 2.5.6 3.6.1.3 0 .7-.2 1z"/></svg>
        203-555-0148
      </div>
      <div class="contact__line contact__phone">
        <svg viewBox="0 0 24 24"><rect x="6" y="2" width="12" height="20" rx="2"/></svg>
        203-555-0172
      </div>
    </div>

    <div class="website">www.marrowbyelectric-example.com</div>
  </section>

</body>
</html>
```